WBP Business Cards

I need business cards for "willow bend partners llc" doublesided... logo on the back (also include logo on front)
logo attached to project... i have jpg up.. let me know if you need eps file.
Company Info:
742 East Harlow Avenue, Suite 8D
Chicago, Illinois 60417
facsimile 312-481-2267 (list fax, address, website on all cards.)
www.willowbendpartnersllc.example
Three different people on cards:
Darius K. Whitcomb, CPA MST
Principal
ofc 312-481-3900
mobile 312-574-8816
dariuskwhitcomb@willowbendpartnersllc.example
Peter J. Olundsen, CPA MST
Principal
peterjolundsen@willowbendpartnersllc.example
mobile 708-613-4471
ofc 312-481-3900
Alvin M Crandby
Principal
ofc 312-481-3900
no mobile
alvinmcrandby@willowbendpartnersllc.example
I have multiple projects listed.. see below:
Business cards for willow bend partners llc
letterhead
envelopes
Business cards for KT Holdings LLC
letterhead
envelopes
Target Market(s)
rich people
Industry/Entity Type
Business
Look and feel

```html
<!DOCTYPE html>
<html lang="en">
<head>
<meta charset="utf-8">
<title>Willow Bend Partners LLC — Business Cards</title>
<link href="https://fonts.googleapis.com/css2?family=Cinzel:wght@400&family=Arimo:wght@400&display=swap" rel="stylesheet">
<style>
  :root {
    --navy: #1f3763;
    --navy-text: #2b4476;
    --paper: #e9eaec;
    --ink: #3a3d44;
    --backdrop: #d9d6d1;
    --white: #f4f5f7;
  }
  * { margin: 0; padding: 0; box-sizing: border-box; }
  html, body {
    width: 1200px; height: 900px; overflow: hidden;
    background: var(--backdrop);
  }
  .sheet {
    position: relative; width: 1200px; height: 900px;
    display: flex; flex-direction: column; align-items: center; justify-content: center; gap: 60px;
  }
  .card {
    position: relative; width: 560px; height: 320px;
    box-shadow: 0 6px 18px rgba(0,0,0,0.18);
  }
  /* Back side */
  .card--back { background: var(--navy); }
  .card--back .wordmark {
    position: absolute; left: 0; right: 0; top: 50%; transform: translateY(-50%);
    text-align: center;
    font-family: "Cinzel", serif; font-weight: 400; font-size: 26px; letter-spacing: 1.5px;
    color: var(--white);
  }
  /* Front side */
  .card--front { background: var(--paper); }
  .card--front .wordmark {
    position: absolute; left: 30px; top: 178px; width: 240px;
    text-align: center;
    font-family: "Cinzel", serif; font-weight: 400; font-size: 17px; letter-spacing: 0.6px; line-height: 1.3;
    color: var(--navy-text);
  }
  .contact {
    position: absolute; left: 290px; top: 34px; width: 255px;
    font-family: "Arimo", sans-serif; color: var(--ink);
  }
  .contact .name { font-size: 17px; color: var(--navy-text); }
  .contact .title { font-size: 12px; margin-top: 2px; }
  .phones { list-style: none; margin-top: 12px; }
  .phones li { display: flex; align-items: center; gap: 7px; font-size: 11px; line-height: 17px; }
  .phones svg { width: 12px; height: 12px; flex: none; }
  .email, .address, .web { font-size: 10px; }
  .email { margin-top: 14px; }
  .address { margin-top: 12px; line-height: 14px; }
  .web { margin-top: 6px; color: var(--navy-text); }
  .band {
    position: absolute; left: 0; right: 0; bottom: 22px; height: 20px;
    background: var(--navy);
  }
</style>
</head>
<body>
<main class="sheet">
  <section class="card card--back" aria-label="Card back">
    <div class="wordmark">Willow Bend Partners LLC</div>
  </section>

  <section class="card card--front" aria-label="Card front">
    <div class="wordmark">Willow Bend Partners LLC</div>

    <div class="contact">
      <div class="name">Darius K. Whitcomb, CPA MST</div>
      <div class="title">Principal</div>
      <ul class="phones">
        <li>
          <svg viewBox="0 0 12 12" aria-label="office"><circle cx="6" cy="6" r="6" fill="#1f3763"/><path d="M3.6 3.2c.4-.4.8-.3 1 .1l.5.9c.2.3.1.6-.2.8l-.3.2c.3.7.9 1.3 1.6 1.6l.2-.3c.2-.3.5-.4.8-.2l.9.5c.4.2.5.6.1 1-.8.8-2.2.4-3.5-.9S2.8 4 3.6 3.2z" fill="#fff"/></svg>
          312-481-3900
        </li>
        <li>
          <svg viewBox="0 0 12 12" aria-label="fax"><circle cx="6" cy="6" r="6" fill="#1f3763"/><rect x="3" y="5" width="6" height="3.5" rx=".6" fill="#fff"/><rect x="4" y="3" width="4" height="2" fill="#fff"/></svg>
          312-481-2267
        </li>
        <li>
          <svg viewBox="0 0 12 12" aria-label="mobile"><circle cx="6" cy="6" r="6" fill="#1f3763"/><rect x="4.2" y="2.6" width="3.6" height="6.8" rx=".6" fill="#fff"/><rect x="4.8" y="3.4" width="2.4" height="4.4" fill="#1f3763"/></svg>
          312-574-8816
        </li>
      </ul>
      <div class="email">dariuskwhitcomb@willowbendpartnersllc.example</div>
      <div class="address">742 East Harlow Avenue, Suite 8D<br>Chicago, Illinois 60417</div>
      <div class="web">www.willowbendpartnersllc.example</div>
    </div>

    <div class="band"></div>
  </section>
</main>
</body>
</html>
```